Cover art needed for best LASIK patient education book ever written!

Help us design a an outstanding cover for this book:
Clear Sight Ahead?
Hidden Truths for Picking a Trustworthy Refractive Specialist
By Walter B. Hensley, MD and
Derek T. Oswalt
We give you nine chapters of easy-to-understand explanations about how LASIK may, or may not, help improve you vision. In addition, we offer tell-all secrets and insider tips on how to tell whether the LASIK center is doing what is best for your vision, or for their financial performance. If you have ever considered LASIK laser vision correction, this book is required reading before you make a decision.
So what do you say? Will you draw a great cover for our book? By the way, preferred colors include jewel tones like deep purple and royal blue.
Requirements
Must have
- Book Title
- Subtitle
- Outstanding Graphics
- Walter B. Hensley, MD (main author) should be in slightly larger font than Derek T. Oswalt (secondary author)
- compelling art that makes you want to pick up the book
Should not have
- no blood, image representing pain, or anything else that would generally not appeal to patients

```html
<!DOCTYPE html>
<html lang="en">
<head>
<meta charset="utf-8">
<title>Clear Sight Ahead? — Book Cover</title>
<link href="https://fonts.googleapis.com/css2?family=Montserrat:wght@300;400&family=Cormorant+Garamond:wght@600;700&display=swap" rel="stylesheet">
<style>
  :root {
    --backdrop: #b2b1ae;
    --cover: #3a1f47;
    --cover-deep: #2f1a3b;
    --art-dark: #1c0f22;
    --art-glow: #8a5cc0;
    --art-light: #c9a6ec;
    --text-main: #ffffff;
    --text-soft: #e4dcea;
    --accent-band: #4a0aa6;
  }
  * { margin: 0; padding: 0; box-sizing: border-box; }
  html, body {
    width: 1018px;
    height: 1200px;
    overflow: hidden;
    background: var(--backdrop);
  }
  .canvas {
    position: relative;
    width: 1018px;
    height: 1200px;
  }
  .book-cover {
    position: absolute;
    left: 145px;
    top: 40px;
    width: 728px;
    height: 1120px;
    background: linear-gradient(180deg, var(--cover-deep) 0%, var(--cover) 45%, var(--cover) 100%);
    overflow: hidden;
  }
  .cover-title {
    position: absolute;
    top: 128px;
    left: 0;
    width: 100%;
    text-align: center;
    font-family: "Montserrat", sans-serif;
    font-weight: 400;
    font-size: 72px;
    line-height: 98px;
    letter-spacing: 2px;
    color: var(--text-main);
    text-transform: uppercase;
  }
  .cover-art {
    position: absolute;
    top: 359px;
    left: 0;
    width: 100%;
    height: 377px;
    background:
      radial-gradient(ellipse 18% 30% at 47% 50%, var(--art-light) 0%, rgba(138,92,192,0.55) 45%, transparent 75%),
      radial-gradient(ellipse 48% 42% at 52% 50%, rgba(138,92,192,0.45) 0%, rgba(60,30,80,0.3) 60%, transparent 85%),
      linear-gradient(90deg, #3a2442 0%, var(--art-dark) 40%, var(--art-dark) 100%);
  }
  .cover-subtitle {
    position: absolute;
    top: 786px;
    left: 60px;
    width: 608px;
    text-align: center;
    font-family: "Montserrat", sans-serif;
    font-weight: 300;
    font-size: 24px;
    line-height: 34px;
    letter-spacing: 1px;
    color: var(--text-soft);
  }
  .cover-authors {
    position: absolute;
    top: 1000px;
    left: 0;
    width: 100%;
    text-align: center;
    font-family: "Cormorant Garamond", serif;
    text-transform: uppercase;
    color: var(--text-soft);
  }
  .author-main {
    font-weight: 700;
    font-size: 16px;
    letter-spacing: 6px;
    line-height: 26px;
  }
  .author-second {
    margin-top: 10px;
    font-weight: 600;
    font-size: 12px;
    letter-spacing: 5px;
    line-height: 18px;
  }
  .accent-band {
    position: absolute;
    left: 0;
    bottom: 0;
    width: 100%;
    height: 31px;
    background: var(--accent-band);
  }
</style>
</head>
<body>
  <div class="canvas">
    <section class="book-cover">
      <h1 class="cover-title">Clear Sight<br>Ahead?</h1>
      <div class="cover-art" role="img" aria-label="Glowing purple network illustration of an eye made of connected points and lines on a dark background"></div>
      <p class="cover-subtitle">Hidden Truths for Picking a Trustworthy Refractive Specialist</p>
      <div class="cover-authors">
        <p class="author-main">Walter B. Hensley, MD</p>
        <p class="author-second">Derek T. Oswalt</p>
      </div>
      <div class="accent-band"></div>
    </section>
  </div>
</body>
</html>
```